Kit Darvell - health and fitness coach who needs a web page. simple and effective

I am a online health and fitness coach who runs a 10 week challenge 4 times a year. I am wanting, a menu with a bit about me, a place where people can buy the programme, testimonies, memberships, photos, and recipes.
I am wanting it to look modern, professional and simple.
The website is how potential clients can check out the memberships for the programme, photos of myself and and my family to show members that I am a confident, educated, independent and healthy woman. Who is very passionate about making a difference in people lives to become a better version of themselves.
My training philosophy is simple, Commitment to training, Consistently working hard and training equals Change! Change is physical changes to the body!!

Target Market(s)

Woman 25-44 years

Industry/Entity Type

Health And Wellness

Coding

Coded - Design and coding required

Number of Pages Required

5+ page

Font styles to use
Sans Serif

Colors
fbed22
e667a6
ffffff

Requirements
Must have
• I like the style of "plain tile" website design.
• On the menu bar I want 9 different tabs/options to click on, these are named:
• BLOG
• ABOUT
• TRAINING PROGRAMS
• HEALTHY FOOD
• SUBSCRIBE
• TESTIMONIALS
• CHATWALL
• SNAPLOOMER
• VID REEL
Nice to have
• logo at the top (attached under file 2)
• Easy for myself to add information once website design is completed.
• lots of white space, white a bright yellow (same as logo) or pink
Should not have
• clutter

```html
<!DOCTYPE html>
<html lang="en">
<head>
<meta charset="utf-8">
<title>Memberships – Kit Darvell</title>
<link href="https://fonts.googleapis.com/css2?family=Montserrat:wght@300;500;600;700&family=Open+Sans:wght@400;600;700&display=swap" rel="stylesheet">
<style>
  :root {
    --yellow: #fbed22;
    --nav-yellow: #fff76b;
    --band-yellow: #f9fb0c;
    --pink: #ff69b4;
    --soft-pink: #ffc0cb;
    --ink: #111111;
    --muted: #333333;
    --line: #e4e4e4;
    --foot-grey: #f5f5f5;
    --chatwall: #3b5998;
    --snaploomer: #c13584;
    --vidreel: #ff0000;
    --gold: #e8b32a;
  }
  * { box-sizing: border-box; margin: 0; padding: 0; }
  html, body { width: 1200px; height: 1130px; overflow: hidden; background: #fff; }
  body { position: relative; font-family: "Montserrat", sans-serif; color: var(--ink); }
  a { color: inherit; text-decoration: none; }

  .brand { position: absolute; left: 0; top: 0; width: 1200px; height: 108px; display: flex; align-items: center; justify-content: center; }
  .brand-name { font-family: "Montserrat", sans-serif; font-weight: 300; font-size: 40px; color: var(--yellow); letter-spacing: 1px; }

  .main-nav { position: absolute; left: 0; top: 108px; width: 1200px; height: 54px; background: var(--nav-yellow); display: flex; align-items: center; }
  .nav-dots { position: absolute; left: 5px; top: 19px; width: 4px; }
  .nav-dots span { display: block; width: 4px; height: 4px; border-radius: 50%; background: var(--ink); margin-bottom: 2.5px; }
  .nav-links { position: absolute; left: 66px; display: flex; gap: 27px; list-style: none; }
  .nav-links li { font-size: 13.5px; font-weight: 500; letter-spacing: 2px; }
  .nav-links .current { color: var(--gold); }
  .nav-tools { position: absolute; left: 978px; top: 11px; display: flex; align-items: center; gap: 8px; }
  .cart { position: relative; width: 22px; height: 32px; margin-right: 2px; }
  .cart-count { position: absolute; left: 19px; top: 0; width: 11px; height: 13px; border-radius: 2px; background: var(--gold); color: #fff; font: 600 7px "Open Sans", sans-serif; text-align: center; line-height: 13px; }
  .social { width: 31px; height: 31px; border-radius: 50%; display: block; }
  .social.chatwall { background: var(--chatwall); }
  .social.snaploomer { background: var(--snaploomer); }
  .social.vidreel { background: var(--vidreel); }

  .page-title { position: absolute; left: 66px; top: 228px; font-size: 27px; font-weight: 700; }

  .note { position: absolute; left: 66px; top: 301px; width: 1053px; height: 99px; background: var(--pink); padding: 29px 22px; }
  .note h2 { font-size: 13px; font-weight: 600; margin-bottom: 12px; }
  .note p { font-size: 13.5px; font-weight: 600; }

  .plans { position: absolute; left: 66px; top: 446px; width: 1050px; height: 261px; display: flex; border: 1px solid var(--line); border-bottom: 2px solid #ddd; }
  .plan { flex: 1; border-right: 1px solid var(--line); position: relative; }
  .plan:last-child { border-right: none; }
  .plan-name { text-align: center; font-size: 15px; font-weight: 600; margin-top: 18px; letter-spacing: .3px; }
  .price-band { position: absolute; left: 0; right: 0; top: 91px; height: 55px; background: var(--pink); }
  .price-badge { position: absolute; left: 50%; top: 50px; width: 82px; height: 82px; margin-left: -41px; border-radius: 50%; background: #fff; border: 2px solid var(--line); text-align: center; z-index: 1; }
  .price { font-size: 27px; font-weight: 500; margin-top: 20px; line-height: 1; }
  .price sup { font-size: 12px; font-weight: 600; vertical-align: 9px; margin-right: 2px; }
  .pay { font: 600 8px "Open Sans", sans-serif; color: var(--muted); margin-top: 4px; }
  .term { position: absolute; left: 0; right: 0; top: 146px; height: 34px; background: var(--band-yellow); text-align: center; line-height: 34px; font-size: 13.5px; font-weight: 500; }
  .buy { position: absolute; left: 50%; top: 198px; width: 87px; height: 40px; margin-left: -43px; background: #000; color: #fff; border-radius: 3px; text-align: center; line-height: 40px; font: 600 12.5px "Open Sans", sans-serif; }

  .site-footer { position: absolute; left: 0; top: 785px; width: 1200px; height: 274px; border-top: 1px solid #eee; }
  .footer-brand { position: absolute; left: 72px; top: 77px; font-weight: 300; font-size: 33px; color: var(--yellow); }
  .footer-col { position: absolute; top: 66px; }
  .footer-col h3 { font-size: 17.5px; font-weight: 700; margin-bottom: 18px; }
  .footer-col ul { list-style: none; }
  .footer-col li { font: 400 13.5px "Montserrat", sans-serif; margin-bottom: 20px; font-weight: 500; }
  .quick { left: 336px; }
  .more { left: 876px; }
  .footer-tag { position: absolute; left: 607px; top: 87px; width: 160px; height: 52px; background: var(--soft-pink); text-align: center; line-height: 52px; font-size: 13.5px; font-weight: 500; }

  .bottom-bar { position: absolute; left: 0; top: 1059px; width: 1200px; height: 71px; background: var(--foot-grey); }
  .copyright { position: absolute; left: 66px; top: 26px; font: 700 8.5px "Open Sans", sans-serif; }
  .bottom-social { position: absolute; left: 1003px; top: 17px; display: flex; gap: 9px; }
  .bottom-social .social { width: 32px; height: 32px; }
</style>
</head>
<body>
  <header class="brand">
    <span class="brand-name">Kit Darvell</span>
  </header>

  <nav class="main-nav">
    <div class="nav-dots"><span></span><span></span><span></span></div>
    <ul class="nav-links">
      <li><a href="#">HOME</a></li>
      <li><a href="#">TRAINING PROGRAMS</a></li>
      <li class="current"><a href="#">MEMBERSHIPS</a></li>
      <li><a href="#">CONTACT US</a></li>
      <li><a href="#">TESTIMONIALS</a></li>
      <li><a href="#">ABOUT</a></li>
      <li><a href="#">BLOG</a></li>
    </ul>
    <div class="nav-tools">
      <div class="cart">
        <svg width="20" height="22" viewBox="0 0 20 22" style="position:absolute;left:0;top:10px" aria-label="Cart">
          <path d="M6 8V5a4 4 0 0 1 8 0v3" fill="none" stroke="#111" stroke-width="1.6"/>
          <rect x="1.5" y="8" width="17" height="12.5" fill="none" stroke="#111" stroke-width="1.6"/>
        </svg>
        <span class="cart-count">0</span>
      </div>
      <a class="social chatwall" href="#" aria-label="CHATWALL"></a>
      <a class="social snaploomer" href="#" aria-label="SNAPLOOMER"></a>
      <a class="social vidreel" href="#" aria-label="VID REEL"></a>
    </div>
  </nav>

  <h1 class="page-title">Memberships</h1>

  <section class="note">
    <h2>ACCOUNTABILITY</h2>
    <p>Fitness Tests at the beginning and end of the program to measure your performance over the 10 weeks</p>
  </section>

  <section class="plans">
    <article class="plan">
      <h3 class="plan-name">BASIC</h3>
      <div class="price-band"></div>
      <div class="price-badge"><div class="price"><sup>$</sup>150</div><div class="pay">PayMint</div></div>
      <div class="term">$150 for 10 week</div>
      <a class="buy" href="#">Buy Now</a>
    </article>
    <article class="plan">
      <h3 class="plan-name">STANDARD</h3>
      <div class="price-band"></div>
      <div class="price-badge"><div class="price"><sup>$</sup>280</div><div class="pay">paymint</div></div>
      <div class="term">Two Terms $280</div>
      <a class="buy" href="#">Buy Now</a>
    </article>
    <article class="plan">
      <h3 class="plan-name">PREMIUM</h3>
      <div class="price-band"></div>
      <div class="price-badge"><div class="price"><sup>$</sup>550</div><div class="pay">PayMint</div></div>
      <div class="term">1 Year $550</div>
      <a class="buy" href="#">Buy Now</a>
    </article>
  </section>

  <footer class="site-footer">
    <span class="footer-brand">Kit Darvell</span>
    <div class="footer-col quick">
      <h3>Quick Links</h3>
      <ul>
        <li><a href="#">Home</a></li>
        <li><a href="#">Training Programs</a></li>
        <li><a href="#">Contact Us</a></li>
      </ul>
    </div>
    <a class="footer-tag" href="#">Memberships</a>
    <div class="footer-col more">
      <h3>More Informations</h3>
      <ul>
        <li><a href="#">About</a></li>
        <li><a href="#">Testimonials</a></li>
      </ul>
    </div>
  </footer>

  <div class="bottom-bar">
    <p class="copyright">COPYRIGHT 2018 KIT DARVELL - ALL RIGHTS RESERVED.</p>
    <div class="bottom-social">
      <a class="social chatwall" href="#" aria-label="CHATWALL"></a>
      <a class="social snaploomer" href="#" aria-label="SNAPLOOMER"></a>
      <a class="social vidreel" href="#" aria-label="VID REEL"></a>
    </div>
  </div>
</body>
</html>
```